a book cover that highlights a culture of people not supporting others in their raise to success

I would like to have crabs in a buckets. The faces of the crabs should be replaced with human faces.

This book is about people who are not willing to help others who are moving to the next level in their lives, careers, families or communities. The focus is to offer solutions to those who want to become better persons.

Title CrabologySubtitleHow to recognize and overcome the crab mentality in yourself and othersAuthorJohnny Riley Jr. withArmani Valentino Added Friday, January 16, 2015

Business Community

Moving

Serif

• A sharp presentation

```html
<!DOCTYPE html>
<html lang="en">
<head>
<meta charset="utf-8">
<title>Gullworthy — Book Cover</title>
<link rel="stylesheet" href="https://fonts.googleapis.com/css2?family=Anton&family=Archivo+Black&family=Bodoni+Moda:opsz,wght@6..96,600&display=swap">
<style>
  :root {
    --ink: #111111;
    --accent: #d4202a;
    --paper-light: #ffffff;
    --paper-mid: #e8e8e8;
    --paper-edge: #c6c6c6;
    --frame: #000000;
    --art-warm: #ea5a36;
    --art-deep: #2f4f9a;
    --art-metal: #8d9096;
    --art-metal-dark: #55585e;
  }
  * { margin: 0; padding: 0; box-sizing: border-box; }
  html, body { width: 794px; height: 1200px; overflow: hidden; background: var(--frame); }
  .canvas { position: relative; width: 794px; height: 1200px; background: var(--frame); }
  .cover {
    position: absolute; left: 13px; top: 13px; width: 769px; height: 1068px;
    background: radial-gradient(ellipse 62% 55% at 50% 52%, var(--paper-light) 0%, var(--paper-mid) 70%, var(--paper-edge) 100%);
  }
  .cover-type { position: absolute; left: 0; top: 0; width: 769px; height: 1068px; }
  .title { font-family: "Anton", "Oswald", sans-serif; font-size: 200px; fill: var(--ink); }
  .subtitle { font-family: "Bodoni Moda", "Didot", serif; font-weight: 600; font-size: 36px; fill: var(--ink); }
  .subtitle.highlight { fill: var(--accent); }
  .author { font-family: "Bodoni Moda", "Didot", serif; font-weight: 600; font-size: 30px; fill: var(--ink); }
  .coauthor { font-family: "Archivo Black", "Arial Black", sans-serif; font-size: 21px; fill: var(--ink); }
  .cover-art {
    position: absolute; left: 154px; top: 467px; width: 447px; height: 461px;
    border-radius: 46% 46% 22% 22% / 40% 40% 14% 14%;
    background:
      radial-gradient(ellipse 40% 30% at 42% 30%, #f07a52 0%, transparent 100%),
      linear-gradient(180deg, var(--art-warm) 0%, var(--art-warm) 42%, var(--art-deep) 47%, var(--art-metal) 52%, var(--art-metal-dark) 100%);
  }
</style>
</head>
<body>
<div class="canvas">
  <div class="cover">
    <div class="cover-art" role="img" aria-label="Illustration of a smiling crab with a human face relaxing in a metal bucket of water"></div>
    <svg class="cover-type" viewBox="0 0 769 1068" aria-label="Gullworthy: How to notice and move past the pinch habit in yourself and others, by Marcus Deloach Jr. with Terrence Obuya">
      <text class="title" x="40" y="254" textLength="685" lengthAdjust="spacingAndGlyphs">GULLWORTHY</text>
      <text class="subtitle" x="136" y="340" textLength="498" lengthAdjust="spacingAndGlyphs">HOW TO NOTICE AND MOVE PAST THE</text>
      <text class="subtitle highlight" x="263" y="387" textLength="243" lengthAdjust="spacingAndGlyphs">PINCH HABIT</text>
      <text class="subtitle" x="198" y="435" textLength="372" lengthAdjust="spacingAndGlyphs">IN YOURSELF AND OTHERS</text>
      <text class="author" x="250" y="1024" textLength="265" lengthAdjust="spacingAndGlyphs">MARCUS DELOACH, JR.</text>
      <text class="coauthor" x="191" y="1050" textLength="356" lengthAdjust="spacingAndGlyphs">WITH TERRENCE OBUYA</text>
    </svg>
  </div>
</div>
</body>
</html>
```